Coastline Pulse Fiesta wordpress website

We need a wordpress design for a Brazilian dance festival event to happen in mid August in Sydney Australia.

The elevator pitch for this event is:

"Coastline Pulse Fiest is for the Social dancer who loves Brazilian rhythms and wants to have a space to dance, socialize and be inspired by a more intense experience than a regular class. As opposed to congress & festivals where there is a formality and focus on performances our events focus on relaxed and warm interactions between dance professionals and dance amateurs."

Most dances are originally from Rio de Janeiro-Brazil and we want to emphasize the cultural connection between both cities Rio (Brazil) & Sydney (Australia): beach culture, warm smiley people, love for music, dance and outdoors.

Feel free to contrast flag colours red/white/blue (Australia) & Green/yellow (Brazil)

We do not have a logo and the template / theme will be hosted on Wordpress 3.5.2
Updates

Hi everyone,

Just to let you know we've extended the deadline on this design project.

Good luck

Hi please

1. use the three uploaded pics of couples dancing as a primary feature in a banner across the page.
2. use the colours of brazil - greens, yellows and blues where possible if you have not used already.
3. Do the Heart in We Pulse Fiesta Dance as an actual heart image.

Thanks, looking forward to the revisions.

Cheers

Renato and Jill

Target Market(s)

social dancers- men & women between 25 and 60 yo. The majority of participants are single.

Industry/Entity Type

Festival

Requirements
Must have
• Top menu to be editable via wordpress.
website skeleton top menu (see attached file)
Nice to have
• The theme should be up, lively and fun, yet relaxed and informal.
Should not have
• Any images / sillouettes of samba Carnival women in Feathers.

```html
<!DOCTYPE html>
<html lang="en">
<head>
<meta charset="utf-8">
<title>Brazilian dance festival</title>
<link href="https://fonts.googleapis.com/css2?family=Ubuntu:wght@400;500&family=Arimo:wght@400;700&family=Roboto+Condensed:wght@700&display=swap" rel="stylesheet">
<style>
:root{
  --page:#ffffff;
  --nav:#f7b900;
  --nav-ink:#2a2a1c;
  --nav-active:#e9e6c9;
  --drop:#dcdab4;
  --sky:#55a8d5;
  --sea:#3dbbec;
  --heading:#3b97cf;
  --sub:#333c4a;
  --body:#3d5a80;
  --more:#f2b51c;
  --rule:#d9dde2;
  --footer:#82bde0;
  --foot-head:#e6cf6a;
  --foot-ink:#3a3a2a;
}
*{margin:0;padding:0;box-sizing:border-box}
html,body{width:1200px;height:1000px;overflow:hidden;background:var(--page)}
body{position:relative;font-family:"Arimo",Arial,sans-serif;color:var(--body)}
.abs{position:absolute}

/* top navigation */
.topnav{left:186px;top:0;width:864px;height:20px;background:var(--nav)}
.topnav ul{list-style:none;display:flex;justify-content:center;align-items:center;height:20px;margin-left:40px}
.topnav li{font-family:"Roboto Condensed",sans-serif;font-weight:700;font-size:10px;color:var(--nav-ink);letter-spacing:.2px;padding:0 5px;position:relative}
.topnav li+li::before{content:":";position:absolute;left:-2px;color:#8a6a00}
.topnav li.active{background:var(--nav-active);padding:3px 6px;margin-top:1px}
.dropdown{left:453px;top:17px;width:103px;background:var(--drop);list-style:none}
.dropdown li{font-family:"Roboto Condensed",sans-serif;font-weight:700;font-size:6.5px;color:var(--nav-ink);height:12.5px;line-height:12.5px;padding-left:12px;border-top:1px solid #f3f1dc}

/* header */
.masthead{left:186px;top:20px;width:864px;height:262px;background:var(--sky)}
.hero{left:255px;top:20px;width:710px;height:225px;background:linear-gradient(180deg,#7ec61d 0%,#8cc41a 38%,#c8d40c 50%,#e0dc10 68%,#2b84c0 76%,#1f5f8a 100%)}
.hero-strip{left:255px;top:245px;width:710px;height:37px;background:var(--sea)}
.title-band{left:255px;top:58px;width:710px;height:48px;background:rgba(40,70,10,.35)}
.site-title{left:262px;top:64px;font-family:"Ubuntu",sans-serif;font-weight:500;font-size:29px;color:#fff;letter-spacing:.2px}
.site-tag{left:360px;top:97px;font-family:"Arimo",sans-serif;font-size:12px;color:#fff;letter-spacing:.3px}

/* content */
.col h2{font-family:"Ubuntu",sans-serif;font-weight:400;font-size:24px;color:var(--heading)}
h3{font-family:"Ubuntu",sans-serif;font-weight:500;font-size:15px;color:var(--sub)}
p{font-size:12.4px;line-height:15.2px;color:var(--body)}
.more{color:var(--more)}
hr{border:0;border-top:1px solid var(--rule)}
.photo{background:radial-gradient(ellipse at 45% 60%,#9a4a1c 0%,#5a2a12 35%,#1c1410 75%,#0e0c0c 100%)}
.slider-dots{left:355px;top:563px;width:42px;height:22px;background:rgba(220,230,240,.55);border-radius:4px 4px 0 0}
.slider-dots span{position:absolute;top:7px;width:9px;height:9px;border-radius:50%;background:#2a6f9e}
.btn{left:542px;top:707px;width:135px;height:31px;border-radius:4px;border:1px solid #a9a86a;background:linear-gradient(180deg,#e3e2b6,#b8b774);font-family:"Ubuntu",sans-serif;font-size:14px;color:#2f2f22;text-align:center;line-height:29px}

/* footer */
.footer{left:186px;top:828px;width:864px;height:172px;background:var(--footer)}
.foot-col{text-align:center;font-size:8px;line-height:10px;color:var(--foot-ink)}
.foot-col h4{font-family:"Ubuntu",sans-serif;font-size:9px;font-weight:500;color:var(--foot-head);margin-bottom:13px}
.social span{position:absolute;width:19px;height:19px;border-radius:50%}
.foot-note{left:186px;top:940px;width:864px;text-align:center;font-size:8px;font-weight:700;color:#1e2a3a}
</style>
</head>
<body>

<nav class="abs topnav">
  <ul>
    <li>HOME PAGE</li>
    <li class="active">EVENT INFORMATION</li>
    <li>INSTRUCTOR PROFILES</li>
    <li>TIMETABLE</li>
    <li>TICKETS</li>
    <li>CONTACT US</li>
  </ul>
</nav>

<header>
  <div class="abs masthead"></div>
  <div class="abs hero" role="img" aria-label="Panorama joining Rio's Sugarloaf mountain and Sydney's harbour bridge, tinted in green, yellow and blue bands"></div>
  <div class="abs hero-strip"></div>
  <div class="abs title-band"></div>
  <h1 class="abs site-title">Brazilian dance festival</h1>
  <div class="abs site-tag">nononononononononononononon</div>
</header>

<ul class="abs dropdown">
  <li>DANCE STYLES</li>
  <li>WORKSHOPS</li>
  <li>PARTIES</li>
  <li>PERFORMANCES</li>
</ul>

<section class="abs col" style="left:235px;top:336px;width:272px">
  <h2>Information</h2>
  <h3 style="margin-top:14px">Probably The Best Company</h3>
</section>
<div class="abs photo" style="left:235px;top:406px;width:272px;height:180px" role="img" aria-label="Close-up of a violin body and strings"></div>
<div class="abs slider-dots"><span style="left:7px"></span><span style="left:25px"></span></div>
<div class="abs" style="left:235px;top:599px;width:272px">
  <p>Vestibulum fermentum faucibus augue aptent et lectus. Lacus amet morbi id posuere vestibulum arcu suspendisse mollis lobortis tincidunt praesent nec imperdiet velit.</p>
  <p style="margin-top:9px">Pharetra adipiscing praesent augue ipsum ac vel nam ante blandit. Nibh arcu quam magna sapien. Quisque mauris morbi pede blandit hendrerit mollis.</p>
  <p class="more" style="margin-top:10px">Continue...</p>
</div>

<section class="abs col" style="left:542px;top:336px;width:253px">
  <h2>Services</h2>
  <h3 style="margin-top:14px">Strategic Planning</h3>
  <p style="margin-top:11px">Imperdiet aenean a ullamcorper. Sed eleifend mollis eu tincidunt fusce accumsan quam lobortis metus sit.<span class="more">Mais...</span></p>
  <hr style="margin-top:24px">
  <h3 style="margin-top:12px">Marketing Consulting</h3>
  <p style="margin-top:11px">In at metus id sit felis consectetuer luctus ac. Nisl ut justo mi quam et enim dolor dapibus vestibulum adipiscing auctor.<span class="more">Mais...</span></p>
  <hr style="margin-top:24px">
  <h3 style="margin-top:12px">Financial Analysis</h3>
  <p style="margin-top:11px">Orci tempus nisl ac eget. Donec dolor vivamus vestibulum velit arcu id pellentesque tincidunt orci ante congue at.<span class="more">Mais...</span></p>
</section>
<div class="abs btn">See All Services</div>

<section class="abs col" style="left:833px;top:336px;width:194px">
  <h2>Notícias</h2>
  <h3 style="margin-top:14px">04/01/2011</h3>
  <p style="margin-top:11px">Nisi libero eleifend torquent eros rutrum curabitur at. Justo laoreet placerat ante.</p>
  <hr style="margin-top:9px">
  <h3 style="margin-top:12px">04/01/2011</h3>
  <p style="margin-top:11px">Ante scelerisque vestibulum posuere egestas amet purus vestibulum cras metus ipsum nullam odio vel sed.</p>
  <hr style="margin-top:9px">
  <h3 style="margin-top:12px">04/01/2011</h3>
  <p style="margin-top:11px">Ac arcu quam hendrerit hendrerit nonummy litora nisi tortor lacus. Euismod augue malesuada sit.</p>
  <hr style="margin-top:9px">
  <h3 style="margin-top:12px">04/01/2011</h3>
  <p style="margin-top:11px">malesuada hendrerit quis ut ac ullamcorper turpis dolor hac nunc. Ut felis ut laoreet quis.</p>
</section>

<footer>
  <div class="abs footer"></div>
  <div class="abs foot-col" style="left:350px;top:854px;width:80px">
    <h4>Information</h4>Organization<br>Schedule<br>Pessoas<br>Management
  </div>
  <div class="abs foot-col" style="left:458px;top:854px;width:80px">
    <h4>Localização</h4>Area Map<br>Address<br>Contact Us
  </div>
  <div class="abs foot-col" style="left:585px;top:854px;width:80px">
    <h4>Company</h4>About Us<br>Terms
  </div>
  <div class="abs social" style="left:795px;top:865px">
    <span style="left:0;background:#e8731c"></span>
    <span style="left:26px;background:#3b5b9a"></span>
    <span style="left:52px;background:#3fa9dd"></span>
  </div>
  <div class="abs foot-note">texto texto texto texto texto</div>
</footer>

</body>
</html>
```